Business Card Design

I would like a new business card that incorporates the new colors and font of the attached DKM4x10.pdf file of our new sign (latte & luxurious red from Kelvane Fairbrook colors) with the logo from the old business card (file name is New2014.pdf). You can remove the phrases from the old card, and just use the contact info provided above. Please let me know if you have any questions.

Industry/Entity Type

Business

Contact Information for Business Card

Dana Kay Morrow, LLC
Real Estate Attorney
842 Larkspur Street
Cedar Hollow, GA 30599
(O) 555-203-4179
(C) 555-372-9051
dana@dkmlawoffice.com
dkmlawoffice.com

```html
<!DOCTYPE html>
<html lang="en">
<head>
<meta charset="utf-8">
<title>Dana Kay Morrow, LLC — Business Card</title>
<link rel="stylesheet" href="https://fonts.googleapis.com/css2?family=Arvo:wght@400;700&family=PT+Sans:wght@400;700&display=swap">
<style>
  :root {
    --page: #e6e2dc;
    --latte: #f0ebe2;
    --luxe-red: #b85a69;
    --luxe-red-deep: #a8485a;
    --ink-light: #fbf4f2;
    --rule-light: rgba(255, 244, 242, 0.75);
  }
  * { box-sizing: border-box; margin: 0; padding: 0; }
  html, body {
    width: 1200px;
    height: 780px;
    overflow: hidden;
    background: var(--page);
  }
  .canvas {
    width: 1200px;
    height: 780px;
    display: flex;
    align-items: center;
    justify-content: center;
  }
  .card {
    width: 1050px;
    height: 600px;
    background: var(--latte);
    display: flex;
    flex-direction: column;
    box-shadow: 0 6px 18px rgba(0, 0, 0, 0.12);
  }
  .card__brand {
    flex: 0 0 330px;
    display: flex;
    flex-direction: column;
    align-items: center;
    justify-content: center;
    color: var(--luxe-red-deep);
    font-family: "Arvo", Georgia, serif;
  }
  .brand__name {
    font-weight: 700;
    font-size: 64px;
    letter-spacing: 0.5px;
    line-height: 1;
  }
  .brand__rule {
    width: 420px;
    height: 2px;
    background: var(--luxe-red-deep);
    margin: 22px 0 14px;
  }
  .brand__tagline {
    font-weight: 700;
    font-size: 26px;
    letter-spacing: 0.5px;
  }
  .card__band {
    flex: 1;
    background: var(--luxe-red);
    display: flex;
    align-items: center;
    justify-content: center;
    color: var(--ink-light);
    font-family: "PT Sans", Arial, sans-serif;
  }
  .contact-person {
    text-align: right;
    font-size: 29px;
    line-height: 1.2;
    padding-right: 34px;
  }
  .contact-person__name {
    font-weight: 700;
    font-size: 34px;
  }
  .band__divider {
    width: 2px;
    height: 160px;
    background: var(--rule-light);
  }
  .contact-lines {
    list-style: none;
    padding-left: 34px;
    font-size: 29px;
    line-height: 1.2;
  }
  .contact-lines li {
    display: flex;
    align-items: center;
    gap: 14px;
  }
  .contact-icon {
    width: 26px;
    height: 26px;
    flex: 0 0 26px;
  }
</style>
</head>
<body>
<main class="canvas">
  <article class="card">
    <header class="card__brand">
      <h1 class="brand__name">Dana Kay Morrow, LLC</h1>
      <div class="brand__rule"></div>
      <p class="brand__tagline">Real Estate Attorney</p>
    </header>

    <section class="card__band">
      <div class="contact-person">
        <p class="contact-person__name">Dana Kay</p>
        <p>Managing Director</p>
        <p>842 Larkspur Street</p>
        <p>Cedar Hollow, GA 30599</p>
      </div>
      <div class="band__divider"></div>
      <ul class="contact-lines">
        <li>
          <svg class="contact-icon" viewBox="0 0 26 26" aria-hidden="true">
            <rect width="26" height="26" rx="3" fill="#fbf4f2"/>
            <path d="M8 6c1 0 2 2.5 2 3.2 0 .8-1.3 1.2-1.3 2 0 1.2 2.8 4.4 4.3 4.4.8 0 1.2-1.3 2-1.3.7 0 3.2 1 3.2 2 0 1.5-1.6 3-3.2 3C10 19.3 6.7 14 6.7 9.5 6.7 7.7 7.2 6 8 6z" fill="#b85a69"/>
          </svg>
          <span>555-203-4179</span>
        </li>
        <li>
          <svg class="contact-icon" viewBox="0 0 26 26" aria-hidden="true">
            <rect width="26" height="26" rx="3" fill="#fbf4f2"/>
            <rect x="8.5" y="4.5" width="9" height="17" rx="1.5" fill="none" stroke="#b85a69" stroke-width="1.8"/>
            <circle cx="13" cy="18.5" r="1" fill="#b85a69"/>
          </svg>
          <span>555-372-9051</span>
        </li>
        <li>
          <svg class="contact-icon" viewBox="0 0 26 26" aria-hidden="true">
            <rect width="26" height="26" rx="3" fill="#fbf4f2"/>
            <rect x="5" y="7.5" width="16" height="11" fill="none" stroke="#b85a69" stroke-width="1.8"/>
            <path d="M5 7.5l8 6.5 8-6.5" fill="none" stroke="#b85a69" stroke-width="1.8"/>
          </svg>
          <span>dana@dkmlawoffice.com</span>
        </li>
        <li>
          <svg class="contact-icon" viewBox="0 0 26 26" aria-hidden="true">
            <rect width="26" height="26" rx="3" fill="#fbf4f2"/>
            <circle cx="13" cy="13" r="7.5" fill="none" stroke="#b85a69" stroke-width="1.6"/>
            <ellipse cx="13" cy="13" rx="3.2" ry="7.5" fill="none" stroke="#b85a69" stroke-width="1.4"/>
            <path d="M5.5 13h15M7 9h12M7 17h12" stroke="#b85a69" stroke-width="1.3"/>
          </svg>
          <span>dkmlawoffice.com</span>
        </li>
      </ul>
    </section>
  </article>
</main>
</body>
</html>
```